St Louis Electrician Needing a Business Card Design!!

We are a St Louis based electrical contracting firm that needs help designing a business card. We have a logo and I have another image that I would like to incorporate. Open to ideas..Thanks!!

Industry/Entity Type

Business

Requirements
Must have
• there are two downloads...one is the logo and the other is what i was wanting coming off the logo...the light rays. Like the logo with the blue background...Was thinking the whole card would be that color blue.
Should not have
• No lightning bolts

```html
<!DOCTYPE html>
<html lang="en">
<head>
<meta charset="utf-8">
<title>Halvorsen Wiring – Business Card</title>
<link href="https://fonts.googleapis.com/css2?family=Open+Sans:wght@300;400;600;700&display=swap" rel="stylesheet">
<style>
  :root {
    --page-bg: #e9e7e3;
    --card-white: #f7f7f6;
    --divider-grey: #c9cbce;
    --blue-deep: #0b5fb0;
    --blue-mid: #2a86d0;
    --blue-light: #63b3e6;
    --brand-ink: #3d4a57;
    --text-white: #ffffff;
    --text-soft: #e3f0fb;
  }
  * { box-sizing: border-box; margin: 0; padding: 0; }
  html, body {
    width: 1200px; height: 909px; overflow: hidden;
    background: var(--page-bg);
    font-family: "Open Sans", Arial, sans-serif;
  }
  .card {
    position: absolute;
    left: 100px; top: 169px;
    width: 1000px; height: 571px;
    background: var(--card-white);
    box-shadow: 0 10px 30px rgba(0,0,0,0.18);
    overflow: hidden;
  }
  .card__brand-area {
    position: absolute; left: 0; top: 0;
    width: 100%; height: 330px;
    display: flex; align-items: center; justify-content: center;
  }
  .brand {
    display: flex; align-items: center; gap: 16px;
  }
  .brand__mark {
    width: 20px; height: 20px;
    background: var(--brand-ink);
  }
  .brand__name {
    font-size: 52px; font-weight: 600; letter-spacing: 0;
    color: var(--brand-ink);
  }
  .card__divider {
    position: absolute; left: 0; top: 330px;
    width: 100%; height: 22px;
    background: var(--divider-grey);
  }
  .card__info-band {
    position: absolute; left: 0; top: 352px;
    width: 100%; height: 219px;
    background: linear-gradient(100deg, var(--blue-light) 0%, var(--blue-mid) 45%, var(--blue-deep) 100%);
    color: var(--text-white);
  }
  .person {
    position: absolute; left: 48px; bottom: 42px;
  }
  .person__name { font-size: 40px; font-weight: 700; line-height: 1.1; }
  .person__role { font-size: 28px; font-weight: 300; color: var(--text-soft); }
  .contacts {
    position: absolute; right: 60px; top: 34px;
    list-style: none;
  }
  .contacts__item {
    display: flex; align-items: center; gap: 14px;
    font-size: 27px; font-weight: 400; line-height: 48px;
    white-space: nowrap;
  }
  .contacts__icon { width: 22px; height: 22px; flex: none; }
</style>
</head>
<body>
  <div class="card">
    <div class="card__brand-area">
      <div class="brand">
        <span class="brand__mark"></span>
        <span class="brand__name">Halvorsen Wiring Co.</span>
      </div>
    </div>
    <div class="card__divider"></div>
    <div class="card__info-band">
      <ul class="contacts">
        <li class="contacts__item">
          <svg class="contacts__icon" viewBox="0 0 24 24" fill="#fff"><path d="M6.6 2.5l3 3.6-1.8 2.4c1.2 2.6 3.1 4.5 5.7 5.7l2.4-1.8 3.6 3-1.6 3.3c-8.2-.6-14.3-6.7-14.9-14.9z"/></svg>
          555 014 2267
        </li>
        <li class="contacts__item">
          <svg class="contacts__icon" viewBox="0 0 24 24" fill="none" stroke="#fff" stroke-width="2"><circle cx="12" cy="12" r="10"/><ellipse cx="12" cy="12" rx="4.5" ry="10"/><line x1="2" y1="12" x2="22" y2="12"/></svg>
          www.danielmorrow.com
        </li>
        <li class="contacts__item">
          <svg class="contacts__icon" viewBox="0 0 24 24" fill="none" stroke="#fff" stroke-width="2.4"><circle cx="12" cy="12" r="4"/><path d="M16 8v5.5a2.5 2.5 0 0 0 5 0V12a9 9 0 1 0-3.5 7.1"/></svg>
          daniel@halvorsenwiring.com
        </li>
      </ul>
      <div class="person">
        <p class="person__name">Daniel Morrow</p>
        <p class="person__role">Manager</p>
      </div>
    </div>
  </div>
</body>
</html>
```